Refresh of a rather different IT outfit website

Our web site is starting to show it's age. You can see the existing site here: www.plumbcorner.net. As a growing company we want to come across as a dynamic collection of IT experts.

We want to update the design so are open to any colour palette and look, but want to retain our current table logo. We use the logo on our business cards but with a white background - see the attached file, so you don't need to keep the brown or the green.

The design should consider the range of browsers that will be looking at the site - so please show how it will look on a wide screen laptop and a 768x1024 tablet.

We want to add some pages about our team and their skills, probably with photos of each person on the team.

This is an uncoded project - the PSD files of the design is required, not coding.
Updates

Thanks everyone for the submissions so far.  It's a holiday day in the UK today but we will get some feedback on the designs so far out to you.

Target Market(s)

Architects and other creative types looking for IT support

Industry/Entity Type

Business

Font styles to use
Serif
Sans Serif

Requirements
Must have
• Must look good on a laptop and an iPad.

```html
<!DOCTYPE html>
<html lang="en">
<head>
<meta charset="utf-8">
<title>Plumbcorner – Serious IT Support</title>
<link href="https://fonts.googleapis.com/css2?family=Open+Sans:wght@400;600;700&display=swap" rel="stylesheet">
<style>
:root{
  --plum:#9b0a55;
  --plum-dark:#7e0645;
  --gold:#f0c20c;
  --gold-dark:#e0ab00;
  --text:#6a6a6a;
  --ink:#222;
  --line:#dcdcdc;
  --footer:#f4f4f4;
  --bottom:#242424;
  --link:#2b7bc0;
}
*{box-sizing:border-box;margin:0;padding:0}
html,body{width:1150px;height:1200px;overflow:hidden;background:#fff;font-family:"Open Sans",Arial,sans-serif;color:var(--text)}
.wrap{width:960px;margin:0 auto;position:relative}
/* header */
.site-header{height:102px}
.brand{position:absolute;left:2px;top:28px;display:flex;align-items:center;gap:22px}
.brand-mark{width:50px;height:40px;background:var(--gold)}
.brand-name{font-size:40px;font-weight:600;color:var(--plum);letter-spacing:.5px}
.search{position:absolute;left:630px;top:34px;width:150px;height:31px;border:1px solid #d6d6d6;border-radius:3px;font-size:13px;color:#888;padding:6px 11px}
.search svg{position:absolute;right:7px;top:6px}
.search:after{content:"";position:absolute;right:30px;top:4px;width:1px;height:21px;background:#ddd}
.call{position:absolute;right:38px;top:30px;text-align:right;line-height:1}
.call small{display:block;font-size:15px;color:#777}
.call strong{display:block;font-size:19px;font-weight:400;color:var(--plum);margin-top:4px}
.call-icon{position:absolute;right:0;top:36px}
/* nav */
.main-nav{height:46px;background:linear-gradient(var(--plum),var(--plum-dark))}
.main-nav ul{list-style:none;display:flex;height:46px}
.main-nav li{font-size:14px;font-weight:600;color:#fff;line-height:46px;padding:0 25px 0 23px}
.main-nav li.active{background:var(--gold);color:var(--plum);padding:0 25px}
.main-nav li:nth-child(n+3){padding-left:26px;padding-right:25px}
/* hero */
.hero-band{background:#ececec;padding:4px 0 0}
.hero{height:278px;background:linear-gradient(90deg,#a6a6a6 0%,#9b9b9b 45%,#8a99a4 62%,#6e7a82 80%,#3e3e42 100%);position:relative}
.hero h1{position:absolute;left:27px;top:83px;font-size:26px;font-weight:400;color:#333}
.hero .btn{position:absolute;left:28px;top:123px;width:90px;height:32px;background:#fff;border-radius:3px;font-size:13px;color:#555;text-align:center;line-height:32px}
.dots{position:absolute;left:28px;top:229px;width:97px;height:23px;background:#666;border-radius:12px;display:flex;gap:11px;padding:6px 0 0 14px}
.dots span{width:10px;height:10px;border-radius:50%;background:#fff}
.dots span:first-child{background:#666;border:2px solid #fff}
/* intro */
.intro{display:flex;justify-content:space-between;padding-top:28px;height:320px}
.welcome{width:715px}
h2{font-size:23px;font-weight:600;color:var(--plum);margin-bottom:14px}
.welcome p{font-size:13.2px;line-height:22px;margin-bottom:8px}
.more{font-size:12px;font-weight:600;color:#111;margin-top:20px;display:flex;align-items:center;gap:5px}
.services{width:220px}
.services ul{list-style:none}
.services li{height:40px;margin-bottom:2px;background:linear-gradient(var(--gold),var(--gold-dark));border-radius:2px;display:flex;align-items:center;gap:14px;padding-left:14px;font-size:16.5px;font-weight:600;color:var(--plum)}
/* partners */
.partners{border-top:1px solid var(--line);height:105px;display:flex;justify-content:space-between;align-items:center;padding:0 14px}
.partners span{font-size:19px;font-weight:600;color:#8a8a8a}
/* footer */
.site-footer{background:var(--footer);height:240px}
.footer-cols{display:flex;padding-top:26px}
.col{height:198px;border-right:1px solid var(--line)}
.col:last-child{border:none}
.col h3{font-size:17px;font-weight:400;color:#333;margin-bottom:14px}
.company{width:236px}
.company p{font-size:12.3px;line-height:20px;margin-bottom:8px}
.company .dark{color:#111}
.blog{width:265px;padding-left:25px}
.blog h4{font-size:13px;font-weight:600;color:#333;margin-bottom:2px}
.blog p{font-size:12.3px;line-height:20px}
.blog a{font-size:12.3px;color:var(--link);text-decoration:none;display:block;margin-top:4px}
.links{width:245px;padding-left:45px}
.links ul{list-style:none;columns:2;column-gap:0;width:180px;font-size:12.3px;line-height:26px}
.connect{padding-left:28px}
.connect ul{list-style:none}
.connect li{display:flex;align-items:center;gap:10px;height:40px;font-size:12.3px}
.connect i{width:26px;height:26px;background:#3a6fa8;border-radius:3px;display:block}
.connect b{font-size:14.5px;font-weight:400;color:#2f5f9e}
.bottom{background:var(--bottom);height:106px;text-align:center;color:#bbb;font-size:12.3px;padding-top:28px}
.bottom nav span{margin:0 10px}
.bottom p{margin-top:16px}
</style>
</head>
<body>
<header class="site-header">
  <div class="wrap">
    <div class="brand"><span class="brand-mark"></span><span class="brand-name">plumbcorner</span></div>
    <div class="search">Search
      <svg width="18" height="18" viewBox="0 0 18 18"><circle cx="7" cy="7" r="5.5" fill="none" stroke="#999" stroke-width="2"/><line x1="11" y1="11" x2="16" y2="16" stroke="#999" stroke-width="2.5"/></svg>
    </div>
    <div class="call"><small>Call us</small><strong>020 7946 0213</strong></div>
    <svg class="call-icon" width="30" height="26" viewBox="0 0 30 26"><path d="M4 3c2-2 5 2 6 4s-2 3-1 5 4 5 6 5 2-3 4-2 5 3 3 6-6 3-10 0S4 12 3 8s-1-3 1-5z" fill="#888"/><path d="M20 5a6 6 0 0 1 5 5M20 1a10 10 0 0 1 9 9" stroke="#aaa" fill="none" stroke-width="1.5"/></svg>
  </div>
</header>

<nav class="main-nav">
  <div class="wrap">
    <ul>
      <li class="active">HOME</li><li>ABOUT US</li><li>WHAT WE DO</li><li>NEWS BLOG</li><li>ARTICLES</li><li>CLIENTS</li><li>PARTNERS</li><li>CONTACT US</li>
    </ul>
  </div>
</nav>

<section class="hero-band">
  <div class="wrap hero" role="img" aria-label="Businessman touching a glowing digital interface with circular holographic rings">
    <h1>Serious IT Support for business</h1>
    <div class="btn">Read more</div>
    <div class="dots"><span></span><span></span><span></span><span></span></div>
  </div>
</section>

<main class="wrap">
  <section class="intro">
    <div class="welcome">
      <h2>Welcome to Plumbcorner</h2>
      <p>Plumbcorner was established with a specific aim: to consistently deliver an advanced and comprehensive IT service for ambitious growing companies across many industry sectors. We aim to provide the very best in service and support, and to aid business growth through the effective and skilled use of modern IT solutions.</p>
      <p>Founded in 2003, we have grown rapidly and have delivered successful business solutions to small and medium sized businesses, working with customers across a wide IT spectrum. The knowledge, experience and expertise which we have gained managing systems and networks for a range of companies over many years enables us to develop with confidence, the best IT solution for our clients.</p>
      <div class="more">KNOW MORE <svg width="6" height="9"><path d="M0 0l6 4.5L0 9z" fill="#111"/></svg></div>
    </div>
    <aside class="services">
      <h2>Our Services</h2>
      <ul>
        <li><svg width="26" height="26" viewBox="0 0 26 26"><circle cx="13" cy="13" r="10" fill="none" stroke="#5a3a00" stroke-width="5"/><circle cx="13" cy="13" r="10" fill="none" stroke="var(--gold)" stroke-width="5" stroke-dasharray="6 9.7"/></svg>SUPPORT</li>
        <li><svg width="26" height="26" viewBox="0 0 26 26" fill="#5a3a00"><circle cx="9" cy="8" r="5"/><path d="M0 24c0-7 4-10 9-10s9 3 9 10z"/><circle cx="18" cy="7" r="4"/><path d="M19 13c4 0 7 3 7 9h-6c0-4-1-7-3-9z"/></svg>CONSULTANCY</li>
        <li><svg width="26" height="26" viewBox="0 0 26 26" fill="#5a3a00"><circle cx="10" cy="10" r="7" stroke="#5a3a00" stroke-width="4" stroke-dasharray="3 2.5" fill="none"/><circle cx="10" cy="10" r="5"/><circle cx="20" cy="20" r="4"/></svg>CAD</li>
        <li><svg width="26" height="26" viewBox="0 0 26 26"><rect x="2" y="2" width="22" height="22" fill="none" stroke="#5a3a00" stroke-width="2.5"/><path d="M2 9h22M2 16h22" stroke="#5a3a00" stroke-width="2"/></svg>HOSTING</li>
        <li><svg width="26" height="26" viewBox="0 0 26 26" stroke="#5a3a00" stroke-width="3.5" stroke-linecap="round"><path d="M4 4l18 18M22 4L4 22"/></svg>DEVELOPMENT</li>
      </ul>
    </aside>
  </section>

  <section class="partners" aria-label="Our clients">
    <span>Greenmarket</span><span>Searchly</span><span>Proflow</span><span>Ledgerly</span><span>Printora</span><span>Telvia</span><span>Softvale</span><span>Artisoft</span><span>Netrion</span>
  </section>
</main>

<footer class="site-footer">
  <div class="wrap footer-cols">
    <div class="col company">
      <h3>Company Details</h3>
      <p>Plumbcorner.net Ltd<br>Harlow House, 48-52 Marsh Lane,<br>London EC2Q 4LT, United Kingdom</p>
      <p>Registered in the UK: 5128406<br>VAT number: 612 4470 19</p>
      <p class="dark">Telephone : &nbsp;020 7946 0213<br>Fax : &nbsp; 020 7946 0288</p>
    </div>
    <div class="col blog">
      <h3>Latest Blog</h3>
      <h4>Morbi sit amet consequat diam</h4>
      <p>Cras faucibus sapien at arcu dignissim interdum. Sed tempus leo nulla, eget auctor tortor pharetra a. Morbi et gravida tortor, vitae cursus odio amet felis eleifend molestie</p>
      <a href="#">Know more</a>
    </div>
    <div class="col links">
      <h3>Quick Links</h3>
      <ul><li>Home</li><li>About us</li><li>What we do</li><li>News blog</li><li>Articles</li><li>Clients</li><li>Partners</li><li>Contact</li><li>Support</li><li>Terms</li></ul>
    </div>
    <div class="col connect">
      <h3>Connect with us</h3>
      <ul>
        <li><i></i>Join with us on <b>Friendspace</b></li>
        <li><i></i>Follow us on <b>Chirpline</b></li>
        <li><i></i>Share on <b>Proflow</b></li>
        <li><i></i>Watch on <b>Viewstream</b></li>
      </ul>
    </div>
  </div>
</footer>
<div class="bottom">
  <nav><span>Home</span>|<span>About us</span>|<span>What we do</span>|<span>News blog</span>|<span>Articles</span>|<span>Clients</span>|<span>Partners</span>|<span>Contact us</span></nav>
  <p>Copyright &copy; 2014 &nbsp;Plumbcorner. &nbsp;All rights reserved.</p>
</div>
</body>
</html>
```